Hartwell Taproom Co Menu Design

I have an exisiting restaurant called Hartwell Taproom Co. We have an official logo and an existing menu. We need something more professional and vibrant. We are a great little brewpub and need our menu to reflect the same.
Updates

I have added our existing menu that has our logo on first page. Please use and insert menu items and pricing. Thank you for all your help! I really need a great look... also our web site is hartwelltaproomco.comĀ  that may help as well

I have been trying to uplaod pictures for the menu design today but for some reason I can not get them to upload on this site. Will keep trying and hope to have some posted soon.

I have submitted pictures to pixel harbor web administration and they will be posting to my project shortly.

All pictures have been posted for menu design. Thanks!

Industry/Entity Type

Restaurant

Requirements
Must have
• Great layout with pictures!!! Need it to be eye catching with current menu items and pricing. Needs to be a funtional format so I can easily changed to add or delete items as needed. I am looking for a one page menu that is 8 1/2 x 14 with front and back side print that will be placed in a clear menu cover.

```html
<!DOCTYPE html>
<html lang="en">
<head>
<meta charset="utf-8">
<title>Hartwell Taproom Co — Menu</title>
<link rel="stylesheet" href="https://fonts.googleapis.com/css2?family=Satisfy&family=Ultra&family=Open+Sans:wdth,wght@75..100,400..700&display=swap">
<style>
  :root {
    --bg: #000000;
    --ink: #ffffff;
    --gold: #e8a019;
    --rule: #c98a14;
    --accent: #ff5a1a;
    --photo-wings: #8a4a1c;
    --photo-tacos: #8c6a4a;
    --photo-salad: #5a6a3a;
  }
  * { margin: 0; padding: 0; box-sizing: border-box; }
  html, body { width: 728px; height: 1200px; overflow: hidden; background: var(--bg); }
  .menu-page {
    position: relative; width: 728px; height: 1200px; overflow: hidden; background: var(--bg);
    color: var(--ink); font-family: "Open Sans", Tahoma, sans-serif; font-stretch: 85%;
  }
  .brand { position: absolute; left: 10px; top: 16px; display: flex; align-items: center; gap: 6px; }
  .brand-dot { width: 14px; height: 14px; border-radius: 50%; background: var(--gold); }
  .brand-name { color: var(--gold); font-weight: 700; font-size: 13px; line-height: 15px; width: 80px; }
  .page-title {
    position: absolute; left: 0; width: 728px; top: 14px; text-align: center;
    font-family: "Satisfy", cursive; font-size: 50px; font-weight: 400; line-height: 64px; color: var(--ink);
  }
  .section-head { position: absolute; left: 34px; width: 670px; display: flex; align-items: center; gap: 6px; }
  .section-head .rule { height: 3px; background: var(--rule); }
  .section-head .rule.lead { width: 34px; }
  .section-head .rule.tail { flex: 1; }
  .section-head h2 {
    font-family: "Ultra", serif; font-weight: 400; font-size: 19px; letter-spacing: 1px;
    color: var(--gold); text-transform: uppercase; line-height: 20px;
  }
  .dressings {
    position: absolute; left: 75px; top: 773px; font-size: 8.6px; font-weight: 600;
    color: var(--accent); white-space: nowrap;
  }
  .item { position: absolute; left: 36px; width: 690px; font-size: 8.6px; line-height: 12px; white-space: nowrap; }
  .item .price { position: absolute; left: 0; top: 0; font-weight: 600; }
  .item .name { margin-left: 39px; color: var(--gold); font-weight: 600; text-transform: uppercase; }
  .item .name .note { color: var(--accent); text-transform: none; }
  .item .name .aside { color: var(--ink); text-transform: none; }
  .item .desc { margin-left: 38px; font-weight: 600; }
  .photo { position: absolute; border-radius: 4px; }
  .photo.wings { left: 256px; top: 612px; width: 102px; height: 60px; background: radial-gradient(circle at 40% 50%, var(--photo-wings), #2a160a 80%); }
  .photo.tacos { left: 334px; top: 648px; width: 100px; height: 89px; background: radial-gradient(circle at 50% 50%, var(--photo-tacos), #2b2018 80%); }
  .photo.salad { left: 340px; top: 1082px; width: 98px; height: 82px; background: radial-gradient(circle at 50% 50%, var(--photo-salad), #1e2214 80%); }
</style>
</head>
<body>
<main class="menu-page">
  <div class="brand"><span class="brand-dot"></span><span class="brand-name">Hartwell Taproom Co</span></div>
  <h1 class="page-title">Menu</h1>

  <div class="section-head" style="top:124px"><span class="rule lead"></span><h2>Starters</h2><span class="rule tail"></span></div>

  <div class="item" style="top:173px"><span class="price">$6.95</span><div class="name">Mediterranean Bruschetta :</div><div class="desc">Mix of roasted artichoke hearts, roasted tomatoes, queen and black olives, Oregano and olive oil. served with crostini sprinkled with parmesan cheese</div></div>
  <div class="item" style="top:208px"><span class="price">$7.95</span><div class="name">Grilled Salmon Tacos:</div><div class="desc">4 grilled salmon tacos topped with pico de gallo and chipotle sauce ...</div></div>
  <div class="item" style="top:244px"><span class="price">$7.95</span><div class="name">Tinga de Pollo Quesadilla :</div><div class="desc">Grilled chicken is made in a cream sauce with caramelized onions Roasted peppers, smoked jalapeno,Cilantro and Colby jack cheese on a flour tortilla<br>With chipotle and avocado cream sauce ......</div></div>
  <div class="item" style="top:286px"><span class="price">$8.95</span><div class="name">Pork Fries:</div><div class="desc">Shredded pork with caramelized onions and green peppers topped with a spicy Tomato sriracha sauce and provolone cheese ...</div></div>
  <div class="item" style="top:320px"><span class="price">$8.95</span><div class="name">Calamari Provencale:</div><div class="desc">Fried calamari is dressed in a buttery sauce with tomatoes, scallions, Mushrooms, lemon and herbs ...</div></div>
  <div class="item" style="top:355px"><span class="price">$8.95</span><div class="name">Santa Fe Rolls:</div><div class="desc">Crispy tortilla rolls filled with chicken, black beans, fire roasted red peppers, cilantro, sweet corn, Jalapeños and Monterey jack cheese. Served with avocado<br>Cream sauce, then garnished with shredded carrots...</div></div>
  <div class="item" style="top:400px"><span class="price">$8.95</span><div class="name">Buffalo Wings: <span class="note">(Mild or Inferno style!)</span></div><div class="desc">8 large wings marinated in buttery buffalo sauce. Served with carrot and celery sticks and buttermilk ranch dressing...</div></div>
  <div class="item" style="top:434px"><span class="price">$6.95</span><div class="name">Smoke House Mac &amp; Cheese:</div><div class="desc">Creamy and savory....Aged sharp cheddar and smoked Gouda, topped with shredded Colby jack...</div></div>
  <div class="item" style="top:469px"><span class="price">$8.95</span><div class="name">Asian Wings:</div><div class="desc">8 large wings marinated in an orange glaze sauce with just the right amount of spice. Served with Asian slaw made with rice wine vinegar, cabbage mix,<br>Shallots and cilantro ...</div></div>
  <div class="item" style="top:515px"><span class="price">$6.95</span><div class="name">Sweet Potato Fries:</div><div class="desc">Garnished with parmesan and parsley. Served with chipotle ranch for dipping ...</div></div>
  <div class="item" style="top:550px"><span class="price">$7.75</span><div class="name">White Truffle Garlic Parmesan Fries:</div><div class="desc">One of a kind! Golden crispy fries drizzled with white cheese sauce made with garlic and white truff Oil topped with parsley and<br>Shredded parmesan...</div></div>

  <div class="photo wings" role="img" aria-label="Photo of buffalo wings with a glass of beer"></div>
  <div class="photo tacos" role="img" aria-label="Photo of grilled salmon tacos"></div>

  <div class="section-head" style="top:754px"><span class="rule lead"></span><h2>Salad &amp; Soup</h2><span class="rule tail"></span></div>
  <p class="dressings">Available Dressings: Caesar, White Balsamic, Raspberry Balsamic, Thousand Island, Bleu Cheese or Buttermilk Ranch.</p>

  <div class="item" style="top:805px"><span class="price">$11.95</span><div class="name">Chopped Cobb:</div><div class="desc">Tossed to perfection is chopped Romaine with grilled chicken, smoked bacon, diced tomato, onion, Avocado and crumbled bleu cheese...</div></div>
  <div class="item" style="top:839px"><span class="price">$12.95</span><div class="name">Seared Ahi Tuna:</div><div class="desc">Seasoned and seared sushi grade Ahi tuna is served with mixed greens and cabbage tossed in roasted garlic rice wine vinaigrette.<br>Topped with marinated cucumbers and onions, then drizzled with toasted Sesame ginger vinaigrette ...</div></div>
  <div class="item" style="top:887px"><span class="price">$11.95</span><div class="name">Santa Fe Chicken Salad:</div><div class="desc">Mixed greens, diced masquite chicken, shredded Colby jack cheese, Rad onion and fire-roasted red peppers accompanied by our Santa Fe<br>Rolls shredded carrots, Crisp tortilla strips and cilantro then drizzled with chipotle ranch dressing ...</div></div>
  <div class="item" style="top:932px"><span class="price">$11.95</span><div class="name">Calamari Salad:</div><div class="desc">Breaded calamari rings are flash fried and lightly seasoned on top of a bed of spring mix greens ossed in white balsamic vinaigrette,<br>Dicad cucumber, bacon and roasted red peppers ...</div></div>
  <div class="item" style="top:978px"><span class="price">$9.95</span><div class="name">Grilled Chicken Caesar:</div><div class="desc">Romaine lettuce and masquite grilled chicken, focaccia croutons, parmesan cheese and Caesar dressing ...</div></div>
  <div class="item" style="top:1012px"><span class="price">$10.95</span><div class="name">Substitute Grilled Salmon</div></div>
  <div class="item" style="top:1036px"><span class="price">$8.95</span><div class="name">Tossed Caprese Salad:</div><div class="desc">Romaine lettuce is tossed with tomatoes, sliced red onion, basil pesto, shredded mozzarella and parmesan, then drizzled with<br>Halsamic glaze ...</div></div>
  <div class="item" style="top:1080px"><span class="price">$4.95</span><div class="name">House Side Salad:</div><div class="desc">Romaine lettuce, tomato, crumbled bleu cheese ..</div></div>
  <div class="item" style="top:1118px"><span class="price">$5.95</span><div class="name">Soup of the Day<span class="aside">... Just ask any server! ... Bowl..</span></div></div>

  <div class="photo salad" role="img" aria-label="Photo of seared ahi tuna salad"></div>
</main>
</body>
</html>
```